300x600 for 1-800-MED-RIGHTNOW for VITALPEDIA Placement

We offer a Tele-Health product that allows customer to join and speak with a Board Certified Doctor over the Phone, by E-Mail or by Video Conferencing.
We are looking to have a 300x600 banner designed for a specific placement on Vitalpedia.com for our product 1-800-MED-RIGHTNOW and supporting banners that we will use for retargeting viewers of the initial 300x600 banner. This banner ad will be placed on the “Conditions” results page of Vitalpedia.com. (see attached Symptoms Checker file)

We are looking for a banner that will have a high CTR as our audience for this placement will be very targeted. These are people who have gone through all the Symptom Checker qualifying questions to reach a conditions page where they can get a basic idea of their illness. We want to step in at this point and offer them the opportunity to speak with a Doctor over the phone to get real medical/health advice.

You can demo the “Symptoms Checker” function on the Vitalpedia.com website, it’s located in the upper left corner. Simply answer some questions until you get to the “Conditions” page and there is where our 300x600 banner will be shown.

We would like to integrate some simple line art type animation to grab attention. Similar to the popular Weight Loss / Diet Banners (See attached 300x250 Weight Loss Banner). We would like to use this along with some compelling ad copy such as;
A Doctor Visit without Visiting the Doctor
Have questions about your Health?
Get real Medical and Health advice from a Doctor without having to leave the Comfort of your Home.
Speak with a Doctor in the next 20 Minutes to have all your Health Questions answered by a professional

Some good sites for reference are;
1800medrightnow.com
Brightcare.com

Target Market(s)

We are targeting customers who are currently seeking Medical Advice from the Vitalpedia.com symptoms checker.

Industry/Entity Type

Doctor

Requirements
Must have
• Line Art Animations - A Doctor with a ringing phone or a Doctor on a Video Conference Screen

```html
<!DOCTYPE html>
<html lang="en">
<head>
<meta charset="utf-8">
<title>1-800-MED-RIGHTNOW – 300x600 Banner</title>
<link rel="stylesheet" href="https://fonts.googleapis.com/css2?family=Fira+Sans:wght@400;600;700&family=Oswald:wght@600&display=swap">
<style>
  :root {
    --sky-top: #1d80b5;
    --sky-bottom: #0f6797;
    --ink-white: #ffffff;
    --accent-yellow: #f7d31e;
    --accent-lime: #b8d432;
    --band-green: #9cc83c;
    --band-green-dark: #86b52c;
    --faint-mark: rgba(255,255,255,0.08);
    --icon-ink: rgba(255,255,255,0.92);
    --icon-shade: rgba(20,60,90,0.55);
  }
  * { margin: 0; padding: 0; box-sizing: border-box; }
  html, body { width: 1200px; height: 2400px; overflow: hidden; }
  body { font-family: "Fira Sans", Arial, sans-serif; }

  .banner {
    position: relative;
    width: 1200px;
    height: 2400px;
    overflow: hidden;
    background: linear-gradient(180deg, var(--sky-top) 0%, var(--sky-bottom) 100%);
    color: var(--ink-white);
  }

  .backdrop { position: absolute; inset: 0; width: 1200px; height: 2400px; }

  .headline {
    position: absolute;
    left: 40px;
    top: 150px;
    line-height: 1;
    text-shadow: 0 3px 6px rgba(0,0,0,0.25);
  }
  .headline .line { display: block; white-space: nowrap; }
  .headline .line + .line { margin-top: 50px; }
  .headline .small { font-size: 70px; font-weight: 600; }
  .headline .big { font-size: 118px; font-weight: 700; }

  .query-marks {
    position: absolute;
    right: 20px;
    top: 70px;
    font-weight: 700;
    line-height: 1;
    color: var(--ink-white);
    text-shadow: 0 4px 6px rgba(0,0,0,0.3);
    white-space: nowrap;
  }
  .query-marks span { display: inline-block; }
  .query-marks .q1 { font-size: 240px; }
  .query-marks .q2 { font-size: 180px; color: var(--accent-yellow); }
  .query-marks .q3 { font-size: 125px; }

  .portrait {
    position: absolute;
    border-radius: 50%;
    overflow: hidden;
    display: flex;
    align-items: center;
    justify-content: center;
  }
  .portrait-doctor {
    left: -120px; top: 590px;
    width: 720px; height: 720px;
    border: 24px solid var(--accent-yellow);
    background: radial-gradient(circle at 50% 40%, #f4f1ec 0%, #d9d6d0 50%, #aeb5ba 100%);
  }
  .portrait-patient {
    left: 380px; top: 880px;
    width: 900px; height: 900px;
    border: 28px solid var(--accent-lime);
    box-shadow: 0 0 0 14px var(--accent-yellow);
    background: radial-gradient(circle at 45% 45%, #c9a98a 0%, #8e7660 50%, #5a4d42 100%);
  }
  .portrait .call-icon { display: block; }
  .portrait-doctor .call-icon { width: 260px; height: 260px; margin-left: 90px; }
  .portrait-patient .call-icon { width: 300px; height: 300px; margin-right: 160px; }

  .offer {
    position: absolute;
    left: 0; right: 0;
    top: 1810px;
    text-align: center;
    font-size: 58px;
    font-weight: 600;
    line-height: 100px;
    text-shadow: 0 3px 5px rgba(0,0,0,0.3);
  }
  .offer .hl { color: var(--accent-yellow); font-weight: 700; font-size: 76px; }
  .offer .hl-xl { color: var(--accent-yellow); font-weight: 700; font-size: 96px; }

  .phone-band {
    position: absolute;
    left: 0; right: 0; bottom: 0;
    height: 220px;
    background: linear-gradient(180deg, var(--band-green) 0%, var(--band-green-dark) 100%);
    display: flex;
    align-items: center;
    justify-content: center;
  }
  .phone-number {
    font-family: "Oswald", "Arial Narrow", sans-serif;
    font-weight: 600;
    font-size: 122px;
    letter-spacing: 2px;
    color: var(--ink-white);
    text-shadow: 0 3px 6px rgba(0,0,0,0.25);
  }
</style>
</head>
<body>
<main class="banner">
  <svg class="backdrop" viewBox="0 0 1200 2400" aria-hidden="true">
    <g fill="var(--faint-mark)" font-family="Fira Sans, Arial, sans-serif" font-weight="700">
      <text x="20" y="640" font-size="640">?</text>
      <text x="560" y="560" font-size="460">?</text>
      <text x="880" y="1000" font-size="380">?</text>
    </g>
    <polygon points="520,800 1200,640 1200,710 520,870" fill="var(--accent-lime)" opacity="0.85"/>
    <polygon points="0,1500 1200,880 1200,960 0,1580" fill="var(--accent-lime)" opacity="0.9"/>
    <polygon points="0,1610 1200,990 1200,1012 0,1632" fill="var(--accent-yellow)"/>
    <polygon points="0,1665 700,1305 700,1335 0,1695" fill="var(--accent-yellow)"/>
  </svg>

  <h1 class="headline">
    <span class="line"><span class="small">Have </span><span class="big">questions</span></span>
    <span class="line"><span class="small">about your </span><span class="big">Health?</span></span>
  </h1>

  <div class="query-marks" aria-hidden="true"><span class="q1">?</span><span class="q2">?</span><span class="q3">?</span></div>

  <div class="portrait portrait-doctor" role="img" aria-label="Photo of a smiling doctor in a white coat with a stethoscope, talking on a phone">
    <svg class="call-icon" viewBox="0 0 100 100" aria-hidden="true">
      <circle cx="50" cy="50" r="48" fill="var(--icon-shade)"/>
      <path d="M30 24c3-3 7-3 9 0l6 9c2 3 1 6-1 8l-4 3c3 7 9 13 16 16l3-4c2-2 5-3 8-1l9 6c3 2 3 6 0 9l-5 5c-4 4-12 3-22-3-11-7-20-16-26-27-5-9-5-16-1-20z" fill="var(--icon-ink)"/>
      <path d="M60 22a20 20 0 0 1 18 18M58 32a10 10 0 0 1 10 10" stroke="var(--accent-yellow)" stroke-width="4" fill="none" stroke-linecap="round"/>
    </svg>
  </div>
  <div class="portrait portrait-patient" role="img" aria-label="Photo of an unwell woman in a scarf on a couch holding her head and a mobile phone, with a first aid kit">
    <svg class="call-icon" viewBox="0 0 100 100" aria-hidden="true">
      <circle cx="50" cy="50" r="48" fill="var(--icon-shade)"/>
      <rect x="34" y="18" width="32" height="64" rx="6" fill="var(--icon-ink)"/>
      <rect x="38" y="26" width="24" height="44" rx="2" fill="#2a6f99"/>
      <circle cx="50" cy="76" r="3" fill="#2a6f99"/>
      <path d="M72 30a14 14 0 0 1 0 20M78 24a22 22 0 0 1 0 32" stroke="var(--accent-yellow)" stroke-width="4" fill="none" stroke-linecap="round"/>
    </svg>
  </div>

  <p class="offer">
    Get <span class="hl">real Medical</span> and Health advice<br>
    from a <span class="hl-xl">Doctor</span> without having<br>
    to leave the Comfort of your <span class="hl">Home.</span>
  </p>

  <div class="phone-band">
    <span class="phone-number">1-800-MED-RIGHTNOW</span>
  </div>
</main>
</body>
</html>
```